Layout for location based cityguide with social features

I am building Location Based Social network which is basically a cityguide.
So people would see clearly on map location of places and for each place they can read and write reviews and perhaps add pictures.

Current working version can be browsed in
http://beta.townroam.example/maps/english/United%20States/New%20York/10182

To see innerpages
login: plorv / plorv7

Mainly I need:
-first page, with improved category selection bar.

- Rating / review page for business
- settings page for user
+ general infopage for TOS etc.

Please submit also subpages. Users "home" page and company review page. Review page is the most important one after first page.
Example of review page: http://beta.townroam.example/rating/index/7912

Remember that you need to submit 4 designs in this competition.

Target Market(s)

Tourists or information seekers from the city they are browsing.

Shoppers seeking specific brands from city shops, which are open and can serve them with their desired language (i.e. they are tourists in foreign city)

Industry/Entity Type

Building

Requirements
Must have
• I need four pages in this design contest:
1) First page
-First page must display cityname and categories which are selected to be viewed.
-Language selection, possibility to choose another country/city and search.
-category selection
2) Company information page
-needs: opening hours
-which language they can server customers
-short company presentation
-keyword
-brands which are represented
3) Users home page when he logs in
-link to edit own information
-link to follow people / companies
-list of places added / comments leaved
4) general page for TOS etc.

simplicity is a great plus. I like current layout a lot, mainly because only few colours are used and main focus is in map. All functions needed are in one place and rating was placed in bottom of screen so top5 can be increased if needed.

Logo that fits layout and something I could use in prints etc.

When users first comes to page he will instantly get the wow factor + idea of website.

Call to action style functionality.
Nice to have
• I like the current layout where browsing is done from right and rest of the space is reserved for map.

Information that user has logged in.
Top ratings for selected categories

Typical elements of social networks, sharing and feedback etc.
Should not have
• I have tried layouts where there are lots of stuff in everyside of the map.

Earlier examples, don't make site look like this:
http://1.townroam.example
http://2.townroam.example

Map will get lost in the layout, and this is not what I want.

```html
<!DOCTYPE html>
<html lang="en">
<head>
<meta charset="utf-8">
<title>TownRoam – User home</title>
<link href="https://fonts.googleapis.com/css2?family=Lato:ital,wght@0,300;0,400;0,700;0,900;1,400&family=Arimo:ital,wght@0,400;0,700;1,400&display=swap" rel="stylesheet">
<style>
:root{
  --orange:#e4521b;
  --orange-top:#ef6a2a;
  --orange-bottom:#d53f1a;
  --ink:#222;
  --header-grey:#e1e1e1;
  --avatar-grey:#c9c9c9;
  --tab-active:#8c8c8c;
  --tab:#bdbdbd;
  --star-off:#b9b9b9;
  --close:#d93a1c;
  --promo-bg:#232323;
  --map-land:#ede6d8;
  --map-water:#aac3e0;
}
*{box-sizing:border-box;margin:0;padding:0}
html,body{width:1200px;height:636px;overflow:hidden}
body{position:relative;font-family:"Arimo",Arial,sans-serif;color:var(--ink);background:var(--map-land)}

.city-map{position:absolute;inset:0;
  background:
   linear-gradient(112deg,var(--map-water) 0 12%,transparent 12.3%),
   linear-gradient(160deg,transparent 0 62%,var(--map-water) 62.3% 74%,transparent 74.3%),
   var(--map-land);}

.close-btn{position:absolute;width:22px;height:22px;border-radius:50%;background:var(--close);border:2px solid #fff;box-shadow:0 1px 3px rgba(0,0,0,.4)}
.close-btn svg{position:absolute;left:5px;top:5px}

/* promo */
.promo{position:absolute;left:65px;top:20px;width:144px;height:261px;background:var(--promo-bg);border-radius:4px;overflow:hidden;text-align:center;color:#fff}
.promo-art{position:absolute;left:11px;top:7px;width:123px;height:123px;border-radius:50%;background:radial-gradient(circle,#6b4a3a 0 28%,#f4f1ec 30%)}
.promo-line{position:absolute;left:0;right:0;font-family:"Lato",sans-serif;font-weight:700}
.promo-day{top:143px;font-size:13px}
.promo-site{top:161px;font-size:16px}
.promo-name{position:absolute;left:0;right:0;bottom:22px;display:flex;align-items:center;justify-content:center;gap:6px;font-family:"Lato",sans-serif;font-weight:700;font-size:14px;color:#fff}
.promo-name::before{content:"";width:9px;height:9px;background:#f39a1e}

/* profile panel */
.profile{position:absolute;left:223px;top:19px;width:559px;height:583px;border-radius:10px;
  background:linear-gradient(180deg,rgba(255,255,255,.97) 0,rgba(255,255,255,.85) 100%);box-shadow:0 1px 6px rgba(0,0,0,.35)}
.profile-head{position:absolute;left:13px;top:30px;width:500px;height:88px;background:var(--header-grey)}
.avatar{position:absolute;left:0;top:0;width:100px;height:88px;background:var(--avatar-grey)}
.user-name{position:absolute;left:114px;top:14px;font-family:"Lato",sans-serif;font-weight:300;font-size:19px;color:#333}
.user-mail{position:absolute;left:114px;top:41px;font-size:12.5px;color:var(--orange)}
.user-phone{position:absolute;left:114px;top:62px;font-size:12.5px;font-weight:700;color:var(--orange)}
.tabs{position:absolute;left:114px;top:118px;display:flex;gap:2px}
.tab{width:78px;height:20px;border-radius:0 0 5px 5px;background:var(--tab);color:#fff;font-size:9.5px;line-height:20px;text-align:center}
.tab.active{background:var(--tab-active);font-weight:700}
.section-title{position:absolute;left:113px;top:158px;font-family:"Lato",sans-serif;font-size:16px;color:var(--orange)}
.actions{position:absolute;left:111px;top:193px;list-style:none}
.action{height:56px}
.action-top{display:flex;align-items:center;height:20px}
.stars{display:flex;gap:1px;width:58px}
.star{width:11px;height:11px;fill:var(--orange)}
.star.off{fill:var(--star-off)}
.score{width:27px;margin-left:5px;font-family:"Lato",sans-serif;font-weight:900;font-size:18px;color:var(--orange);text-align:center}
.place{margin-left:3px;font-size:11px;font-weight:700;color:var(--orange)}
.quote{margin-top:6px;font-size:11px;font-style:italic;color:#333;white-space:nowrap}

/* sidebar */
.sidebar{position:absolute;left:792px;top:14px;width:184px;height:495px;border-radius:14px;overflow:hidden;
  background:rgba(46,48,52,.9);box-shadow:0 1px 6px rgba(0,0,0,.4)}
.sidebar-top{height:180px;background:linear-gradient(180deg,var(--orange-top),var(--orange-bottom));position:relative}
.brand{position:absolute;left:0;right:0;top:12px;text-align:center;font-family:"Lato",sans-serif;font-weight:900;font-size:21px;color:#fff}
.city-select{position:absolute;left:15px;top:46px;width:152px;height:36px;border-radius:18px;background:#151515;color:#fff;font-family:"Lato",sans-serif;font-size:16px;line-height:36px;padding-left:14px}
.city-select svg,.country svg{position:absolute;top:50%;margin-top:-3px}
.city-select svg{right:14px}
.search{position:absolute;left:18px;top:92px;width:148px;height:26px;border-radius:13px;background:#fff;font-size:9.5px;color:var(--orange);line-height:26px;padding-left:27px}
.search svg{position:absolute;left:10px;top:7px}
.country-label{position:absolute;left:19px;top:130px;font-size:9.5px;font-style:italic;color:#4a1a08}
.country{position:absolute;left:19px;top:144px;font-family:"Lato",sans-serif;font-size:14.5px;color:#fff;padding-right:17px}
.country svg{right:0}
.side-head{position:relative;height:24px;padding-left:11px;font-size:11px;font-weight:700;color:#fff;line-height:24px;
  background:linear-gradient(180deg,#4a4c50,#2f3135);border-top:1px solid #5a5c60}
.side-head::after{content:"";position:absolute;right:11px;top:6px;width:12px;height:12px;border-radius:50%;background:#fff}
.side-head::before{content:"";position:absolute;right:14px;top:11px;width:6px;height:2px;background:#333;z-index:1}
.side-body{padding:12px 11px 17px}
.btn{display:inline-block;height:19px;padding:0 7px;border-radius:3px;background:#1f2023;color:#fff;font-size:8.5px;font-weight:700;line-height:19px;margin-right:3px}
.wish-body{padding:10px 11px 12px}
.wish{list-style:none}
.wish li{font-size:9.5px;font-weight:700;color:var(--orange);line-height:16px;padding-left:12px;position:relative}
.wish li::before{content:"";position:absolute;left:1px;top:5px;width:6px;height:6px;border-radius:50%;background:#fff}
.fav-body{padding:0 0 0 11px}
.empty{font-size:11px;font-style:italic;color:#9a9a9a;padding-top:12px;height:74px;border-bottom:1px solid #5a5c60}
.lang{text-align:center;padding-top:18px;font-size:9.5px;font-style:italic;color:#fff}
.flags{display:flex;justify-content:center;gap:7px;margin-top:7px}
</style>
</head>
<body>

<svg width="0" height="0" style="position:absolute" aria-hidden="true">
  <defs>
    <symbol id="star" viewBox="0 0 11 11"><path d="M5.5 0l1.6 3.5 3.9.4-2.9 2.6.8 3.8-3.4-2-3.4 2 .8-3.8L0 3.9l3.9-.4z"/></symbol>
  </defs>
</svg>

<div class="city-map" role="img" aria-label="Street map of lower Manhattan and the East River"></div>

<aside class="promo">
  <div class="promo-art" role="img" aria-label="Late-night food show artwork"></div>
  <p class="promo-line promo-day">Torstaisin @</p>
  <p class="promo-line promo-site">plattera.example</p>
  <p class="promo-name">Plattera</p>
</aside>
<span class="close-btn" style="left:190px;top:15px"><svg width="8" height="8"><path d="M1 1l6 6M7 1L1 7" stroke="#fff" stroke-width="2"/></svg></span>

<main class="profile">
  <header class="profile-head">
    <div class="avatar" role="img" aria-label="Default user avatar"></div>
    <h1 class="user-name">Testi User</h1>
    <p class="user-mail">username@mailbox.example</p>
    <p class="user-phone">(555)010-3543</p>
  </header>
  <nav class="tabs"><span class="tab active">Actions</span><span class="tab">Reviews</span><span class="tab">Photos</span></nav>
  <h2 class="section-title">Actions</h2>
  <ul class="actions">
    <li class="action"><div class="action-top"><span class="stars"><svg class="star"><use href="#star"/></svg><svg class="star"><use href="#star"/></svg><svg class="star"><use href="#star"/></svg><svg class="star"><use href="#star"/></svg><svg class="star off"><use href="#star"/></svg></span><span class="score">4</span><span class="place">Verde Grove Trattoria</span></div><p class="quote">“The ravioli was superb, will definitely come back for some more!”</p></li>
    <li class="action"><div class="action-top"><span class="stars"><svg class="star"><use href="#star"/></svg><svg class="star"><use href="#star"/></svg><svg class="star"><use href="#star"/></svg><svg class="star"><use href="#star"/></svg><svg class="star"><use href="#star"/></svg></span><span class="score">5</span><span class="place">Halvard Delicatessen</span></div><p class="quote">Lorem ipsum dolor sit amet, consectetur adipiscing elit.</p></li>
    <li class="action"><div class="action-top"><span class="stars"><svg class="star"><use href="#star"/></svg><svg class="star"><use href="#star"/></svg><svg class="star"><use href="#star"/></svg><svg class="star"><use href="#star"/></svg><svg class="star off"><use href="#star"/></svg></span><span class="score">4</span><span class="place">Verde Grove Trattoria</span></div><p class="quote">“The ravioli was superb, will definitely come back for some more!”</p></li>
    <li class="action"><div class="action-top"><span class="stars"><svg class="star"><use href="#star"/></svg><svg class="star"><use href="#star"/></svg><svg class="star"><use href="#star"/></svg><svg class="star"><use href="#star"/></svg><svg class="star"><use href="#star"/></svg></span><span class="score">5</span><span class="place">Halvard Delicatessen</span></div><p class="quote">“The ravioli was superb, will definitely come back for some more!”</p></li>
    <li class="action"><div class="action-top"><span class="stars"><svg class="star"><use href="#star"/></svg><svg class="star"><use href="#star"/></svg><svg class="star"><use href="#star"/></svg><svg class="star"><use href="#star"/></svg><svg class="star off"><use href="#star"/></svg></span><span class="score">4</span><span class="place">Verde Grove Trattoria</span></div><p class="quote">“The ravioli was superb, will definitely come back for some more!”</p></li>
    <li class="action"><div class="action-top"><span class="stars"><svg class="star"><use href="#star"/></svg><svg class="star"><use href="#star"/></svg><svg class="star"><use href="#star"/></svg><svg class="star"><use href="#star"/></svg><svg class="star"><use href="#star"/></svg></span><span class="score">5</span><span class="place">Halvard Delicatessen</span></div><p class="quote">“The ravioli was superb, will definitely come back for some more!”</p></li>
  </ul>
</main>
<span class="close-btn" style="left:756px;top:9px"><svg width="8" height="8"><path d="M1 1l6 6M7 1L1 7" stroke="#fff" stroke-width="2"/></svg></span>

<aside class="sidebar">
  <div class="sidebar-top">
    <p class="brand">TownRoam</p>
    <div class="city-select">New York<svg width="10" height="6"><path d="M0 0h10L5 6z" fill="#fff"/></svg></div>
    <div class="search"><svg width="11" height="12"><circle cx="7" cy="4" r="3.2" fill="none" stroke="#e4521b" stroke-width="1.6"/><path d="M5 6.5L1 11" stroke="#e4521b" stroke-width="1.8"/></svg>Go to address...</div>
    <p class="country-label">Choose country</p>
    <p class="country">United States<svg width="9" height="5"><path d="M0 0h9L4.5 5z" fill="#fff"/></svg></p>
  </div>
  <div class="side-head">Edit profile</div>
  <div class="side-body"><span class="btn">Edit profile</span><span class="btn">Change password</span></div>
  <div class="side-head">Wishlist</div>
  <div class="wish-body"><ul class="wish"><li>Verde Grove Trattoria</li><li>Halvard Delicatessen</li></ul></div>
  <div class="side-head">Favorites</div>
  <div class="fav-body"><p class="empty">The favorites are empty</p></div>
  <div class="lang">Change language
    <div class="flags">
      <svg width="20" height="14" role="img" aria-label="Russian"><rect width="20" height="14" fill="#fff"/><rect y="4.7" width="20" height="4.7" fill="#1c3fa8"/><rect y="9.4" width="20" height="4.6" fill="#d52b1e"/></svg>
      <svg width="20" height="14" role="img" aria-label="Finnish"><rect width="20" height="14" fill="#fff"/><rect x="5" width="3.5" height="14" fill="#1c3f8a"/><rect y="5.3" width="20" height="3.5" fill="#1c3f8a"/></svg>
      <svg width="20" height="14" role="img" aria-label="English"><rect width="20" height="14" fill="#1e3a78"/><path d="M0 0L20 14M20 0L0 14" stroke="#fff" stroke-width="2.6"/><path d="M0 0L20 14M20 0L0 14" stroke="#c8102e" stroke-width="1"/><path d="M10 0v14M0 7h20" stroke="#fff" stroke-width="4"/><path d="M10 0v14M0 7h20" stroke="#c8102e" stroke-width="2.2"/></svg>
    </div>
  </div>
</aside>

</body>
</html>
```